Waste Oil Filter collection & disposal

Basically I need a 1 page website for the business called Canister Recovery Works.
We are a environmental service provider and we collect and dispose of waste oil filters to protect the environment from hazardous waste oil products.

This is the link to our current website: www.canisterrecovery.co.nz

we want it to look fresh and better than our current website. we may potentially look at getting a new logo designed and are open to ideas/designs if you have any.

Industry/Entity Type

Business

Logo Text

Canister Recovery Works

Number of Pages Required

1 page

Requirements
Must have
• same colours as current website.
• description of what service we provide please refer to leaflet attached

```html
<!DOCTYPE html>
<html lang="en">
<head>
<meta charset="utf-8">
<title>Canister Recovery Works</title>
<link href="https://fonts.googleapis.com/css2?family=Lato:wght@300;400;700&display=swap" rel="stylesheet">
<style>
  :root {
    --ink: #0d0d0d;
    --green: #5f8f66;
    --rule: #d6d6d6;
    --paper: #ffffff;
    --muted: #333333;
  }
  * { box-sizing: border-box; margin: 0; padding: 0; }
  html, body { width: 1200px; height: 675px; overflow: hidden; background: var(--paper); }
  body { font-family: "Lato", sans-serif; color: var(--ink); position: relative; }

  .brand { position: absolute; left: 44px; top: 34px; display: flex; align-items: center; gap: 10px; }
  .brand-dot { width: 22px; height: 22px; border-radius: 50%; background: var(--green); }
  .brand-name { font-weight: 700; font-size: 17px; color: var(--ink); letter-spacing: 0.2px; }

  .phone { position: absolute; left: 920px; top: 50px; font-size: 18px; font-weight: 400; letter-spacing: 0.5px; }
  .login {
    position: absolute; left: 1058px; top: 40px; width: 97px; height: 42px;
    border: 2px solid var(--green); display: flex; align-items: center; justify-content: center;
    font-size: 14px; letter-spacing: 0.6px; text-transform: uppercase; color: var(--ink);
  }

  .headline { position: absolute; left: 44px; top: 120px; font-size: 44px; font-weight: 700; line-height: 53px; text-transform: uppercase; }
  .headline span { display: block; white-space: nowrap; }
  .subline { position: absolute; left: 44px; top: 299px; width: 440px; font-size: 25px; font-weight: 400; line-height: 32px; color: var(--green); }
  .divider { position: absolute; left: 44px; top: 390px; height: 1px; width: 536px; background: var(--rule); }
  .summary { position: absolute; left: 44px; top: 417px; width: 542px; font-size: 14.5px; font-weight: 300; line-height: 22px; color: var(--muted); }

  .hours { position: absolute; left: 41px; top: 524px; font-size: 15px; line-height: 22px; }
  .hours-title { font-weight: 700; text-transform: uppercase; }

  .action { position: absolute; top: 608px; display: flex; align-items: center; gap: 22px; font-size: 18px; font-weight: 700; text-transform: uppercase; }
  .action-navigate { left: 41px; }
  .action-email { left: 378px; gap: 17px; }

  .showcase { position: absolute; left: 606px; top: 106px; width: 550px; height: 462px;
    background: linear-gradient(180deg, #2f4a2c 0%, #41613a 35%, #b9bcb6 60%, #6a6d69 100%); }

  .caption { position: absolute; left: 606px; top: 576px; width: 550px; text-align: center; }
  .caption-title { font-size: 15px; text-transform: uppercase; line-height: 20px; }
  .caption-text { font-size: 14px; font-weight: 300; line-height: 20px; color: var(--muted); }
  .caption-arrow { position: absolute; top: 10px; }
  .caption-arrow.prev { left: 0; }
  .caption-arrow.next { right: 0; }

  .legal { position: absolute; left: 0; width: 1200px; top: 658px; text-align: center; font-size: 11px; font-weight: 300; color: var(--muted); }
</style>
</head>
<body>
  <header>
    <div class="brand">
      <span class="brand-dot"></span>
      <span class="brand-name">Canister Recovery Works</span>
    </div>
    <div class="phone">06 555 0142</div>
    <a class="login">Login</a>
  </header>

  <main>
    <h1 class="headline"><span>Specialized in the</span><span>collection &amp; disposal</span><span>of oil / fuel filters</span></h1>
    <p class="subline">Servicing the lower north island on a monthly cycle</p>
    <div class="divider"></div>
    <p class="summary">We offer a cost effective environmentally friendly system for the collection and disposal of waste oil filters helping minimise contamination of landfills keeping your industry compliant.</p>

    <div class="hours">
      <div class="hours-title">Opening hours:</div>
      <div>Monday - Friday (7.30 AM - 5.00 PM)</div>
    </div>

    <a class="action action-navigate">
      <svg width="34" height="40" viewBox="0 0 34 40"><polygon points="0,19 34,0 32,40 20,23" fill="var(--green)"/></svg>
      <span>Navigate now!</span>
    </a>
    <a class="action action-email">
      <svg width="40" height="27" viewBox="0 0 40 27"><rect width="40" height="27" fill="var(--green)"/><polyline points="1,2 20,15 39,2" fill="none" stroke="#fff" stroke-width="2"/></svg>
      <span>Send an email</span>
    </a>

    <div class="showcase" role="img" aria-label="Photo of the purpose built green and grey collection truck parked in front of trees"></div>

    <div class="caption">
      <svg class="caption-arrow prev" width="14" height="28" viewBox="0 0 14 28"><polygon points="14,0 0,14 14,28" fill="var(--green)"/></svg>
      <div class="caption-title">Vehicle</div>
      <div class="caption-text">Purpose built truck for collection</div>
      <svg class="caption-arrow next" width="14" height="28" viewBox="0 0 14 28"><polygon points="0,0 14,14 0,28" fill="var(--green)"/></svg>
    </div>
  </main>

  <footer class="legal">© 2017 Privacy</footer>
</body>
</html>
```